Pinnacle Award Design Project

We have just won an award for customer service and would like to tell our users about how great we are!!

The award is the 3013 National Pinnacle Award for excellence in Customer relations.

We have a in house made banner currently on our home page slider (www.velmorahub.com.au) but we would prefer something more professional.

Homepage Slides (image size: 636 x 313)

```html
<!DOCTYPE html>
<html lang="en">
<head>
<meta charset="utf-8">
<title>National Pinnacle Award – Highly Recommended</title>
<link rel="stylesheet" href="https://fonts.googleapis.com/css2?family=Cormorant+Garamond:ital,wght@0,600;1,600&display=swap">
<style>
  :root {
    --petal-yellow: #f4d70e;
    --petal-light: #f8e64a;
    --flower-core: #e8b80a;
    --leaf-teal: #3aa39a;
    --leaf-green: #5fb27a;
    --panel-yellow: #f1dc1f;
    --panel-teal: #3fa7a3;
    --ink: #111111;
    --ribbon-text: #f1dc1f;
  }
  * { margin: 0; padding: 0; box-sizing: border-box; }
  html, body {
    width: 1200px;
    height: 591px;
    overflow: hidden;
    background: #ffffff;
  }
  .slide {
    position: relative;
    width: 1200px;
    height: 591px;
    overflow: hidden;
    font-family: "Cormorant Garamond", Georgia, serif;
  }
  .flower-photo {
    position: absolute;
    inset: 0;
    background:
      radial-gradient(circle at 320px 290px, var(--flower-core) 0, #efc412 90px, var(--petal-yellow) 210px, transparent 330px),
      radial-gradient(ellipse at 40px 560px, var(--leaf-green) 0, transparent 220px),
      radial-gradient(ellipse at 1180px 560px, var(--leaf-teal) 0, transparent 260px),
      linear-gradient(160deg, var(--petal-light) 0%, var(--petal-yellow) 55%, #e6cf1c 100%);
  }
  .award-panel {
    position: absolute;
    left: 664px;
    top: 34px;
    width: 502px;
    height: 491px;
    background:
      linear-gradient(150deg, var(--panel-yellow) 0%, #eede2c 45%, #9cc45a 70%, var(--panel-teal) 100%);
    box-shadow: -6px 8px 18px rgba(0, 0, 0, 0.45);
    text-align: center;
    color: var(--ink);
  }
  .award-year {
    position: absolute;
    left: 0; right: 0;
    top: 34px;
    font-size: 58px;
    font-weight: 600;
    line-height: 1;
  }
  .award-name {
    position: absolute;
    left: 0; right: 0;
    top: 100px;
    font-size: 76px;
    font-weight: 600;
    line-height: 0.98;
  }
  .award-series {
    position: absolute;
    left: 40px; right: 40px;
    top: 275px;
    font-size: 38px;
    font-weight: 600;
    letter-spacing: 0.55em;
    padding-left: 0.55em;
    line-height: 1;
    border-bottom: 3px solid var(--ink);
    padding-bottom: 6px;
  }
  .award-level {
    position: absolute;
    left: 52px;
    top: 345px;
    width: 398px;
    height: 60px;
    background: var(--ink);
    color: var(--ribbon-text);
    font-size: 40px;
    font-style: italic;
    font-weight: 600;
    line-height: 60px;
  }
  .award-category {
    position: absolute;
    left: 0; right: 0;
    top: 425px;
    font-size: 29px;
    font-style: italic;
    font-weight: 600;
    line-height: 1;
  }
</style>
</head>
<body>
  <main class="slide">
    <div class="flower-photo" role="img" aria-label="Close-up photograph of a bright yellow daisy-like flower against green foliage"></div>
    <section class="award-panel" aria-label="Award announcement">
      <p class="award-year">2013</p>
      <h1 class="award-name">National<br>Pinnacle</h1>
      <p class="award-series">AWARDS</p>
      <p class="award-level">Highly Recommended</p>
      <p class="award-category">Excellence in Customer Service</p>
    </section>
  </main>
</body>
</html>
```